International Lifestyle Real Estate Brokerage Needs Eye Catching Website

We need a new website for a cutting edge / dynamic real estate startup, Pinecrest Realty, that will serve as a concierge brokerage to assist cold weather residents with the research, selection, financing and purchase of vacation / retirement properties in warm weather climates in the US and then globally. We will have personally vetted all properties to insure that our clients are only getting the best of the best with no hidden surprises.

** The website design will ultimately need to be coded into a wordpress theme.

We are not locked into any specific colour scheme but would prefer something warm vs cold as that is really the lifestyle we are selling. We like lots of white negative space and hope to allow high end photography to provide most of the pop in colour.

I have attached mock up wire frames to demonstrate desired functionality for three pages we need designed

1) Home Page
2) Market Profile (City overview and developments)
3) Community Profile Page (Individual development profile)

I have also included .ai file for the logo. Not locked into red.

Final design should communicate excitement, lifestyle while maintaining an air of professionalism and reliability. We have developed over 30 sites and have high expectations for the winning design.

Regards,
Dan
Updates

Project Deadline Extended Reason: Hello,I have been called away from this project for the past couple of weeks and have been unable to get together with the people involved to get a consensus on direction forward. Apologies for the delay - we are still very much committed to moving forward.Regards,Dan Added Wednesday, July 6, 2016

Target Market(s)

Canadian and Northern US residents looking to purchase vacation or retirement real estate in warmer climates, initially in the US, but eventually Internationally.

Industry/Entity Type

Real Estate

Contact Information for Business Card

Names for Business Cards

Dan Whitford
705.555.2147
dan@pinecrestrealty-example.ca

Coding

Coded - Design and coding required

Number of Pages Required

3 page

Font styles to use
Serif
Sans Serif

Requirements
Must have
• See wireframe documents uploaded.
• Site design will ultimately be coded into a child theme to function on a selected wordpress theme. If the designer has a Wordpres Theme in mind that would be compatible with the design we would appreciate that information.
Nice to have
• See wireframe documents uploaded. Prefer clean, modern site, white negative space, bold photography will add most of the colour and pop.
Should not have
• Anything cartoony or sophmoric.

```html
<!DOCTYPE html>
<html lang="en">
<head>
<meta charset="utf-8">
<title>Pinecrest Realty — Home</title>
<link rel="stylesheet" href="https://fonts.googleapis.com/css2?family=Montserrat:ital,wght@0,300;0,400;0,500;0,600;1,400&display=swap">
<style>
:root{
  --red:#e8393b;
  --navy:#1b1440;
  --ink:#1f1a3a;
  --blue:#1d5d8c;
  --grey:#e9e9ec;
  --white:#ffffff;
  --muted:#6b6880;
}
*{box-sizing:border-box;margin:0;padding:0}
html,body{width:1200px;height:2961px;overflow:hidden;background:var(--white)}
body{position:relative;font-family:'Montserrat',sans-serif;color:var(--ink)}
.abs{position:absolute}

/* header */
.utility-nav{left:529px;top:0;width:600px;height:40px;background:var(--navy);display:flex}
.utility-nav span{flex:1;color:#fff;font-size:13px;text-align:center;line-height:40px;border-right:1px solid #3b3560}
.utility-nav span:last-child{border:none}
.brand{left:55px;top:0;width:314px;height:211px;background:var(--red);z-index:2;color:#fff;text-align:center}
.brand-mark{position:absolute;left:132px;top:36px;width:50px;height:50px;border:2px solid #fff;border-radius:50%}
.brand-name{position:absolute;top:108px;width:100%;font-size:38px;font-weight:400;letter-spacing:5px}
.brand-sub{position:absolute;top:156px;width:100%;font-size:14px;letter-spacing:6px}
.main-nav{left:535px;top:94px;width:592px;display:flex;justify-content:space-between;font-size:17px;color:var(--ink)}
.main-nav .sep{color:var(--red)}

/* hero */
.hero{left:0;top:158px;width:1200px;height:513px;background:linear-gradient(160deg,#8e8a96 0%,#5c5866 45%,#a7a3ad 100%)}
.hero-title{left:0;top:300px;width:1200px;text-align:center;color:#fff;font-size:47px;font-weight:400}
.play{left:553px;top:383px}
.hero-sub{left:0;top:498px;width:1200px;text-align:center;color:#fff;font-size:17px}
.hero-btn{left:470px;top:547px;width:260px;height:47px;background:#fff;color:var(--ink);font-size:20px;text-align:center;line-height:47px;font-weight:500}

/* overview */
.overview{left:0;top:671px;width:1200px;height:349px;background:linear-gradient(90deg,#1f1845 0%,#1d4a78 60%,#1d5d8c 100%)}
.overview h2{left:55px;top:714px;color:#fff;font-size:29px;font-weight:400}
.overview-copy{left:55px;top:771px;width:580px;color:#fff;font-size:17px;line-height:21px;font-weight:300}
.btn-pill{height:26px;line-height:26px;font-size:15px;font-style:italic;border-radius:5px;text-align:center}
.btn-learn{left:55px;top:938px;width:119px;background:var(--red);color:#fff}
.btn-register{left:186px;top:938px;width:118px;background:#e6e6ee;color:var(--navy)}
.overview-photo{left:647px;top:776px;width:480px;height:211px;background:linear-gradient(180deg,#c8d6c4 0%,#8f9a86 55%,#3d7fa0 100%)}

/* sections */
.section-title{left:0;width:1200px;text-align:center;font-size:30px;font-weight:400;color:var(--navy)}
.slider{left:55px;top:1155px;width:1072px;height:497px;background:linear-gradient(180deg,#6a5a86 0%,#a08aa6 55%,#5a4a78 100%)}
.arrow{top:1380px}
.accent-bar{left:553px;top:1766px;width:93px;height:10px;background:var(--red)}
.tab{top:1816px;height:56px;line-height:56px;text-align:center;font-size:17px;border:2px solid #c9c9cf;color:var(--navy)}
.tab.active{background:var(--red);border-color:var(--red);color:#fff}
.market{width:331px;height:245px;border:1px solid #d4d4d8}
.market-photo{width:100%;height:100%}
.market-label{position:absolute;left:0;bottom:0;width:100%;height:46px;background:rgba(255,255,255,.85);text-align:center;line-height:46px;font-size:19px;color:var(--navy)}
.commitment{left:795px;top:2215px;width:332px;height:245px;background:var(--red);color:#fff;text-align:center}
.commitment h3{margin-top:48px;font-size:23px;font-weight:400}
.commitment hr{width:76px;margin:10px auto 12px;border:none;height:4px;background:#fff}
.commitment p{font-size:15px;line-height:18px;padding:0 60px}

/* blog */
.blog{left:0;top:2539px;width:1200px;height:290px;background:var(--navy)}
.blog-title{left:0;top:2576px;width:1200px;text-align:center;color:#fff;font-size:30px}
.post{top:2663px;height:101px;display:flex}
.post-date{width:119px;background:#fff;text-align:center;color:var(--navy);padding-top:24px}
.post-date b{display:block;font-size:34px;font-weight:400;line-height:34px}
.post-date small{font-size:12px}
.post-body{flex:1;background:var(--red);color:#fff;font-size:14px;line-height:17px;padding:12px 14px}
.post-body em{display:block;font-weight:600;color:#fde6a8}
.divider{left:591px;top:2663px;width:2px;height:101px;background:#4a4470}
.scroll-tab{left:566px;top:2787px;width:48px;height:42px;background:#2b2450}

/* footer */
.footer{left:0;top:2829px;width:1200px;height:132px;background:var(--grey)}
.footer-lead{left:55px;top:2844px;width:380px}
.footer-lead h4{font-size:18px;font-weight:500;color:var(--navy);line-height:20px}
.footer-lead p{margin-top:8px;font-size:9px;line-height:11px;color:var(--muted)}
.footer-col{top:2844px}
.footer-col h5{font-size:18px;font-weight:400;color:var(--navy);margin-bottom:4px}
.footer-col li{list-style:none;font-size:9px;line-height:12px;color:var(--muted)}
.footer-col li::before{content:"";display:inline-block;width:6px;height:6px;border-radius:50%;background:var(--red);margin-right:4px}
</style>
</head>
<body>

<nav class="abs utility-nav"><span>SAVED</span><span>ABOUT</span><span>CONTACT</span><span>LOGIN</span></nav>
<div class="abs brand">
  <div class="brand-mark"></div>
  <div class="brand-name">PINECREST</div>
  <div class="brand-sub">REALTY</div>
</div>
<nav class="abs main-nav"><span>SEARCH</span><span class="sep">|</span><span>OUR PROCESS</span><span class="sep">|</span><span>RESOURCES</span><span class="sep">|</span><span>REGISTER</span></nav>

<section class="abs hero" role="img" aria-label="Upward view of glass skyscrapers with grid facades"></section>
<h1 class="abs hero-title">LIFE IS TOO SHORT TO BE COLD</h1>
<svg class="abs play" width="90" height="90" viewBox="0 0 90 90"><circle cx="45" cy="45" r="45" fill="#e8393b"/><path d="M36 28 L62 45 L36 62 Z" fill="#fff"/></svg>
<p class="abs hero-sub">Where do you want to play in the sunshine? (advanced search option)</p>
<div class="abs hero-btn">SEARCH</div>

<section class="abs overview"></section>
<h2 class="abs" style="left:55px;top:714px;color:#fff;font-size:29px;font-weight:400">GENERAL OVERVIEW OF SERVICE PROVIDED</h2>
<p class="abs overview-copy">Lorem ipsum dolor sit amet, consectetuer adipiscing elit, sed diam nonummy nibh euismod tincidunt ut laoreet dolore magna aliquam erat volutpat. Ut wisi enim ad minim veniam, quis nostrud exerci tation ullamcorper suscipit lobortis nisl ut aliquip ex ea commodo consequat.<br>Duis autem vel eum iriure dolor in hendrerit.</p>
<div class="abs btn-pill btn-learn">Learn More</div>
<div class="abs btn-pill btn-register">Register CTA</div>
<div class="abs overview-photo" role="img" aria-label="Modern white villa beside a swimming pool"></div>

<h2 class="abs section-title" style="top:1072px">FEATURED DEVELOPMENTS</h2>
<div class="abs slider" role="img" aria-label="Modern two-storey home with pool at dusk"></div>
<svg class="abs arrow" style="left:92px" width="24" height="44" viewBox="0 0 24 44"><path d="M20 4 L4 22 L20 40" fill="none" stroke="#fff" stroke-width="4"/></svg>
<svg class="abs arrow" style="left:1060px" width="24" height="44" viewBox="0 0 24 44"><path d="M4 4 L20 22 L4 40" fill="none" stroke="#fff" stroke-width="4"/></svg>

<h2 class="abs section-title" style="top:1703px">FEATURED MARKETS</h2>
<div class="abs accent-bar"></div>
<div class="abs tab active" style="left:294px;width:190px">UNITED STATES</div>
<div class="abs tab" style="left:505px;width:190px">MEXICO</div>
<div class="abs tab" style="left:717px;width:187px">SOUTH AMERICA</div>

<div class="abs market" style="left:55px;top:1931px"><div class="market-photo" role="img" aria-label="Downtown glass towers under blue sky" style="background:linear-gradient(180deg,#9cc0e4,#3f6f8c)"></div><div class="market-label">ORLANDO</div></div>
<div class="abs market" style="left:424px;top:1931px"><div class="market-photo" role="img" aria-label="Glass tower viewed from below" style="background:linear-gradient(180deg,#b9d2e6,#6e8ea6)"></div><div class="market-label">ORLANDO</div></div>
<div class="abs market" style="left:795px;top:1931px"><div class="market-photo" role="img" aria-label="Steel roof structure from below" style="background:linear-gradient(180deg,#3b3b3b,#8a8a8a)"></div><div class="market-label">ORLANDO</div></div>
<div class="abs market" style="left:55px;top:2215px"><div class="market-photo" role="img" aria-label="White high-rise among trees" style="background:linear-gradient(180deg,#b8d4ec,#7b8a84)"></div><div class="market-label">ORLANDO</div></div>
<div class="abs market" style="left:424px;top:2215px"><div class="market-photo" role="img" aria-label="Curved modern building facade" style="background:linear-gradient(180deg,#4f6f6a,#c7a872)"></div><div class="market-label">ORLANDO</div></div>
<div class="abs commitment"><h3>OUR COMMITMENT</h3><hr><p>Lorem ipsum dolor sit amet, consectetur adipiscing elit. Donec nec lectus tellus. Praesent id nunc blandit, lacinia nunc at</p></div>

<section class="abs blog"></section>
<h2 class="abs blog-title">RECENT BLOG POSTS</h2>
<article class="abs post" style="left:55px;width:519px">
  <div class="post-date"><b>SAT</b><small>15 NOV '15</small></div>
  <div class="post-body">LOREM IPSUM DOLOR SIT AMET, CONSEC-TETUER ADIPISCING ELIT, SED DIAM NONUMMY NIBH EUISMOD TINCIDUNT UT LAOREET<em>READ MORE</em></div>
</article>
<div class="abs divider"></div>
<article class="abs post" style="left:632px;width:495px">
  <div class="post-date"><b>MON</b><small>17 NOV '15</small></div>
  <div class="post-body">LOREM IPSUM DOLOR SIT AMET, CONSEC-TETUER ADIPISCING ELIT, SED DIAM NONUMMY NIBH EUISMOD TINCIDUNT UT LAOREET<em>READ MORE</em></div>
</article>
<svg class="abs scroll-tab" width="48" height="42" viewBox="0 0 48 42"><path d="M15 10 L24 19 L33 10 M15 20 L24 29 L33 20" fill="none" stroke="#e8393b" stroke-width="3"/></svg>

<footer class="abs footer"></footer>
<div class="abs footer-lead">
  <h4>LOREM IPSUM DOLOR SIT AMET, CON-SECTETUER ADIPISCING ELIT</h4>
  <p>LOREM IPSUM DOLOR SIT AMET, CONSECTETUER ADIPISCING ELIT, SED DIAM NONUMMY NIBH EUISMOD TINCIDUNT UT LAOREET DOLORE MAGNA ALIQUAM ERAT VOLUTPAT.</p>
</div>
<div class="abs footer-col" style="left:509px"><h5>ABOUT US</h5><ul><li>CAREERS</li><li>GALLERY</li><li>RECENT WORK</li><li>PRODUCTS</li><li>EVENTS</li><li>SHOW</li></ul></div>
<div class="abs footer-col" style="left:677px"><h5>SUPPORT</h5><ul><li>CAREERS</li><li>GALLERY</li><li>RECENT WORK</li><li>PRODUCTS</li><li>EVENTS</li><li>SHOW</li></ul></div>
<div class="abs footer-col" style="left:861px"><h5>CONTACT US</h5><ul><li>CAREERS</li><li>GALLERY</li><li>RECENT WORK</li><li>PRODUCTS</li><li>EVENTS</li><li>SHOW</li></ul></div>
<div class="abs footer-col" style="left:1032px"><h5>ABOUT US</h5><ul><li>CAREERS</li><li>GALLERY</li><li>RECENT WORK</li><li>PRODUCTS</li><li>EVENTS</li><li>SHOW</li></ul></div>

</body>
</html>
```